Premium B2B Equipment Flyer & Catalog Design

We need a premium industrial B2B print design system for Brondale Strainers, Inc.

Brondale is a premium U.S. manufacturer of solid/liquid pressure filtration equipment, focused on long-term support, custom engineering, QEVN quality, and process partnership.

The goal is to create a professional 8 to 12 page catalog where each product page can also be exported as an individual product flyer for our main equipment lines. The style should feel engineered, reliable, American-made, technical, clean, and premium. It should not look like a cheap or generic equipment flyer.

For the initial design submission, please provide a 2-page sample concept:

One product page using either:
https://brondalestrainers.example/horizontal-plate-filter/standard-horizontal-plate-filter/

or
https://brondalestrainers.example/vertical-plate-filter-main/tvkn/

AND

One company/about page using content from pages such as Who We Are, Engineering, About Us, or similar pages on our website.

Please use www.BrondaleStrainers.example
as the primary source for product information, company background, photos, and branding.

The winning designer should expect to continue working with us after the award to develop the full catalog and individual product flyers across multiple Brondale product lines.

```html
<!DOCTYPE html>
<html lang="en">
<head>
<meta charset="utf-8">
<title>Brondale Strainers — Catalog Spread</title>
<link href="https://fonts.googleapis.com/css2?family=Montserrat:ital,wght@0,400;0,500;0,600;0,700;0,800;1,400&display=swap" rel="stylesheet">
<style>
  :root{
    --bg:#e3e3e4;
    --paper:#ffffff;
    --paper-soft:#f4f5f7;
    --navy:#263a6b;
    --ink:#4a5675;
    --blue:#1d5dbf;
    --blue-deep:#1749a3;
    --gold:#a9832b;
    --white:#ffffff;
  }
  *{box-sizing:border-box;margin:0;padding:0}
  html,body{width:1200px;height:840px;overflow:hidden}
  body{background:var(--bg);font-family:"Montserrat",sans-serif;color:var(--ink);position:relative}
  .spread{position:absolute;left:30px;top:17px;width:1140px;height:806px;display:flex;box-shadow:0 10px 30px rgba(0,0,0,.12)}
  .page{position:relative;width:570px;height:806px;overflow:hidden}
  .page--about{background:var(--paper)}
  .page--product{background:linear-gradient(180deg,#fafbfc 0%,var(--paper-soft) 100%)}
  .folio{position:absolute;top:0;right:0;width:64px;height:64px}
  .folio span{position:absolute;right:8px;top:10px;color:var(--white);font-size:11px;font-weight:700}
  h2{font-weight:700;color:var(--navy);text-transform:uppercase;letter-spacing:.06em;font-size:15px;line-height:1.15}
  p{font-size:8.6px;line-height:1.5}
  .about-intro{position:absolute;left:40px;top:52px;width:440px}
  .about-intro h2{margin-bottom:8px}
  .about-intro .block+.block{margin-top:26px}
  .collage{position:absolute;left:0;top:0}
  .collage text{font-family:"Montserrat",sans-serif;font-weight:700;font-size:10px;letter-spacing:.06em;fill:var(--white)}

  .product-head{position:absolute;left:36px;top:40px;width:290px}
  .product-head h2{font-size:14.5px;margin-bottom:8px}
  .product-head sup{font-size:8px}
  .product-visual{position:absolute;left:340px;top:84px;width:180px;height:130px;border-radius:6px;background:linear-gradient(120deg,#d6d9de 0%,#aeb4bd 45%,#2f6fd0 70%,#1d58b8 100%)}
  .application{position:absolute;left:36px;top:210px;width:268px;height:380px;background:linear-gradient(160deg,var(--blue) 0%,var(--blue-deep) 100%);padding:22px 22px;color:var(--white)}
  .application h2{color:var(--white);margin-bottom:10px}
  .application p{font-size:8.3px;margin-bottom:9px}
  .features{position:absolute;left:322px;top:228px;width:222px}
  .features>h2{margin-bottom:12px}
  .feature{display:flex;gap:10px;margin-bottom:11px}
  .feature svg{flex:0 0 34px}
  .feature h3{font-size:8.6px;font-weight:700;color:var(--navy);text-transform:uppercase;letter-spacing:.04em;margin-bottom:3px}
  .feature p{font-size:7.9px;line-height:1.45}
  .specs{position:absolute;left:36px;top:664px;width:500px}
  .specs h2{margin-bottom:8px}
  .specs p{font-size:8.3px;margin-bottom:3px}
  .specs b{color:var(--navy)}
</style>
</head>
<body>
<div class="spread">

  <section class="page page--about">
    <div class="about-intro">
      <div class="block">
        <h2>Who We Are</h2>
        <p>For nearly a century, Brondale Strainers® has been the trusted leader in industrial liquid-solid separation. Headquartered just outside Halverton, Texas, USA, we manufacture high-quality filtration equipment built to QEVN and Ferrow Vessel Board certification standards, delivering unmatched reliability and performance across a range of industries.</p>
      </div>
      <div class="block">
        <h2>What Sets Us Apart?<br>Engineered for Excellence</h2>
        <p>Our products are designed for long-term performance, with many of our filters remaining in operation for generations under ordinary conditions. We offer custom-built solutions to fit the specific needs of our customers across industries such as:</p>
      </div>
    </div>

    <svg class="collage" width="570" height="806" viewBox="0 0 570 806">
      <defs>
        <linearGradient id="g-chem" x1="0" y1="0" x2="1" y2="1"><stop offset="0" stop-color="#c9d7ea"/><stop offset="1" stop-color="#4f7fc2"/></linearGradient>
        <linearGradient id="g-pharma" x1="0" y1="0" x2="1" y2="1"><stop offset="0" stop-color="#6d79c9"/><stop offset="1" stop-color="#c98ac8"/></linearGradient>
        <linearGradient id="g-food" x1="0" y1="0" x2="1" y2="1"><stop offset="0" stop-color="#3b4a2a"/><stop offset="1" stop-color="#b86a2a"/></linearGradient>
        <linearGradient id="g-mine" x1="0" y1="0" x2="1" y2="1"><stop offset="0" stop-color="#9cc4e6"/><stop offset="1" stop-color="#1d3350"/></linearGradient>
        <linearGradient id="g-toll" x1="0" y1="0" x2="1" y2="1"><stop offset="0" stop-color="#2d3540"/><stop offset="1" stop-color="#8a6e58"/></linearGradient>
      </defs>
      <polygon role="img" aria-label="Photo of a lab technician handling chemical processing equipment" points="0,330 255,378 225,505 0,460" fill="url(#g-chem)"/>
      <polygon role="img" aria-label="Photo of scientists in protective gear in a pharmaceutical lab" points="265,380 445,414 408,562 235,508" fill="url(#g-pharma)"/>
      <polygon role="img" aria-label="Photo of a food and beverage spread on a table" points="455,416 570,438 570,628 418,566" fill="url(#g-food)"/>
      <polygon role="img" aria-label="Photo of a miner silhouetted in an icy cave" points="0,470 222,516 150,806 0,806" fill="url(#g-mine)"/>
      <polygon role="img" aria-label="Photo of a hand signing a contract on a clipboard" points="232,518 404,572 570,638 570,806 160,806" fill="url(#g-toll)"/>

      <g transform="translate(18,432) rotate(10.7)"><rect width="150" height="20" fill="#1d5dbf"/><text x="10" y="14">CHEMICAL PROCESSING</text></g>
      <g transform="translate(262,476) rotate(10.7)"><rect width="112" height="20" fill="#1d5dbf"/><text x="10" y="14">PHARMA &amp; BIO</text></g>
      <g transform="translate(430,530) rotate(10.7)"><rect width="140" height="20" fill="#1d5dbf"/><text x="10" y="14">FOOD &amp; BEVERAGE</text></g>
      <g transform="translate(10,742) rotate(10.7)"><rect width="134" height="20" fill="#1d5dbf"/><text x="10" y="14">MINING &amp; METALS</text></g>
      <g transform="translate(300,744) rotate(10.7)"><rect width="230" height="20" fill="#1d5dbf"/><text x="10" y="14">TOLLING &amp; CONTRACT SOLUTIONS</text></g>
    </svg>

    <div class="folio">
      <svg width="64" height="64" viewBox="0 0 64 64"><polygon points="0,0 64,0 64,64" fill="var(--gold)"/></svg>
      <span>01</span>
    </div>
  </section>

  <section class="page page--product">
    <div class="product-head">
      <h2>Brondale<sup>®</sup> Legacy<br>Horizontal Plate Filter (HPF)</h2>
      <p>Introducing the Brondale® Standard Flow Horizontal Plate Filter (HPF)—our flagship filtration solution is internationally renowned for its versatility, efficiency, and cost-effectiveness. Designed to cater to a wide array of industrial applications, the Standard Flow HPF is the preferred choice for processes requiring reliable, repeatable and efficient filtration.</p>
    </div>

    <div class="product-visual" role="img" aria-label="Product photo of a stainless steel and a blue horizontal plate filter"></div>

    <div class="application">
      <h2>Application</h2>
      <p>With over 20,000 Brondale® Horizontal Plate Filters in operation worldwide, our filters have been tested and proven across thousands of unique applications. Standard Flow HPF's versatility enables it to excel in chemical processing, food and beverage, contract manufacturing/tolling, precious metal recovery and pharmaceutical industries.</p>
      <p>This filter is particularly well-suited for processes involving diatomaceous earth (DE) and activated carbon, achieving ultrafine filtration with micron efficiencies below 1 micron in nearly all liquid/solid applications requiring 0.01–100 micron filtration and ~0.001–20% solids. The Standard Flow HPF delivers unmatched consistency, high-performance separation, and the lowest operating cost of any filtration technology. It's the proven, dependable choice trusted across industries.</p>
      <p>Curious if we've handled your specific application? With decades of expertise, the answer is almost always "yes." Contact us today to discuss how the Standard Flow HPF can alleviate your separation anxiety.</p>
    </div>

    <div class="features">
      <h2>Key Features</h2>
      <div class="feature">
        <svg width="34" height="34" viewBox="0 0 34 34"><circle cx="17" cy="17" r="16" fill="#fff" stroke="#9aa3b8"/><path d="M9 12h16M9 17h16M9 22h16" stroke="var(--navy)" stroke-width="1.6"/></svg>
        <div><h3>Enhanced Filtration Capacity</h3><p>Designed with multiple horizontal filter plates, the Standard Flow HPF significantly increases filter area and cake capacity, ensuring optimal performance and minimal footprint across various applications.</p></div>
      </div>
      <div class="feature">
        <svg width="34" height="34" viewBox="0 0 34 34"><circle cx="17" cy="17" r="16" fill="#fff" stroke="#9aa3b8"/><rect x="10" y="10" width="6" height="6" fill="none" stroke="var(--navy)"/><rect x="18" y="10" width="6" height="6" fill="none" stroke="var(--navy)"/><rect x="10" y="18" width="6" height="6" fill="none" stroke="var(--navy)"/><rect x="18" y="18" width="6" height="6" fill="var(--navy)"/></svg>
        <div><h3>Customizable Options</h3><p>Offering a broad range of materials of construction—including Stainless Steel, Corvalloy, Carbon Steel, rubber lining and more—the HPF and filters media can be tailored to meet specific process requirements and chemical compatibility.</p></div>
      </div>
      <div class="feature">
        <svg width="34" height="34" viewBox="0 0 34 34"><circle cx="17" cy="17" r="16" fill="#fff" stroke="#9aa3b8"/><path d="M8 22l9-11 9 11z" fill="none" stroke="var(--navy)" stroke-width="1.4"/></svg>
        <div><h3>Versatility</h3><p>Ideal for batch-type filtration processes, this filter maintains maximum cake stability, remaining unaffected start and stop or process flow variations.</p></div>
      </div>
      <div class="feature">
        <svg width="34" height="34" viewBox="0 0 34 34"><circle cx="17" cy="17" r="16" fill="#fff" stroke="#9aa3b8"/><circle cx="17" cy="17" r="7" fill="none" stroke="var(--navy)" stroke-width="1.4"/></svg>
        <div><h3>Efficient Cleaning and Maintenance</h3><p>Designed for quick cleaning and re-dressing, downtime is minimized to approximately 15–45 minutes for smaller models and 30–60 minutes for larger units. Optional spare cartridges and bottom equipment are available to further reduce maintenance time.</p></div>
      </div>
    </div>

    <div class="specs">
      <h2>Technical Specifications</h2>
      <p><b>Sizes</b> : Available in standard diameters of 8", 14", 18", 33", and 44" with customization options to fit specific application needs.</p>
      <p><b>Filter Media compatibility</b> : Accommodates various filter media, including filter paper, synthetic materials such as polypropylene, wire mesh, and membrane filter media.</p>
      <p><b>Specification Options</b> : Include cake capacity, filter area, flow rate, filter media, design pressure, differential pressure, and more. Click here for a complete description of specifications and options.</p>
    </div>

    <div class="folio">
      <svg width="64" height="64" viewBox="0 0 64 64"><polygon points="0,0 64,0 64,64" fill="var(--gold)"/></svg>
      <span>02</span>
    </div>
  </section>

</div>
</body>
</html>
```